The BVR in BVR Medical, LLC stands for "Bona Via Regit" a latin term meaning "The good path guides."

I would like to see the letters "BVR" pretty prominent and would like to see something unique like script, definitely not block letters. Color wise I really like purple. As far as additional information goes I'm open to single or double sided. I'm also very open to letting you interject your own creativity, so if you have an idea that involves other colors or creative ways of making the "BVR Medical, LLC" name stand out please submit.

Target Market(s)

Surgeons

Industry/Entity Type

Medical

Contact Information for Business Card

Dale Hopkins, Owner
Mobile - 901-555-0147
Email - bvrmedllc@fernpostmail.com

Logo Text

BVR Medical, LLC

Colors
6b449b
876aae

Requirements
Must have
• Business name, my name and contact information.
Nice to have
• I would like the see the BVR very prominently on the face of the card. BVR Medical, LLC can be in standard type under the large BVR logo or in type near my contact info. I would like to place the logos of the companies I represent. I can provide those once I settle on a design. Just need to be able to add those to the provided file and would like to be able to modify the contact info and logo placement on the back of the card if possible. Although I've chosen colors I'm open to different colors if your designs warrant.

```html
<!DOCTYPE html>
<html lang="en">
<head>
<meta charset="utf-8">
<title>BVR Medical, LLC — Business Card</title>
<link rel="stylesheet" href="https://fonts.googleapis.com/css2?family=PT+Serif:wght@400;700&display=swap">
<style>
  :root {
    --purple-deep: #6b449b;
    --purple-soft: #876aae;
    --purple-pale: #a28cc4;
    --ink: #1d1d1d;
    --paper: #ffffff;
    --backdrop: #ecebef;
  }
  * { box-sizing: border-box; margin: 0; padding: 0; }
  html, body {
    width: 1200px; height: 1024px; overflow: hidden;
    background: var(--backdrop);
    font-family: "PT Serif", Georgia, serif;
  }
  .sheet {
    width: 1200px; height: 1024px;
    display: flex; flex-direction: column; align-items: center; justify-content: center;
    gap: 56px;
  }
  .card {
    position: relative;
    width: 760px; height: 434px;
    background: var(--paper);
    border-radius: 30px;
    overflow: hidden;
    box-shadow: 0 6px 18px rgba(40, 20, 70, 0.18);
  }
  .card__wave { position: absolute; inset: 0; width: 100%; height: 100%; }

  .brand {
    position: absolute; left: 64px; top: 58px;
    color: var(--purple-deep);
    font-weight: 400;
  }
  .brand__initials {
    display: block;
    font-size: 112px; line-height: 0.9; letter-spacing: 2px;
  }
  .brand__name {
    display: block;
    font-size: 34px; line-height: 1.1; letter-spacing: 1px;
    margin-top: 4px; margin-left: 40px;
  }
  .divider {
    position: absolute; left: 372px; top: 150px;
    width: 2px; height: 70px;
    background: linear-gradient(to bottom, rgba(107,68,155,0), var(--purple-deep), rgba(107,68,155,0));
  }
  .person { position: absolute; left: 64px; top: 300px; }
  .person__name {
    color: var(--purple-deep); font-weight: 700; font-size: 30px; line-height: 1.1;
  }
  .person__role { color: var(--ink); font-size: 22px; margin-top: 4px; }

  .contact {
    position: absolute; left: 420px; top: 46px;
    list-style: none;
    color: var(--ink); font-size: 19px; line-height: 1.6;
  }
  .contact__item { display: flex; align-items: center; gap: 10px; }
  .contact__icon { width: 15px; height: 15px; flex: none; }
</style>
</head>
<body>
<main class="sheet">

  <section class="card card--front" aria-label="Card front">
    <svg class="card__wave" viewBox="0 0 760 434" aria-hidden="true">
      <path d="M760,52 C720,210 580,270 490,330 C440,364 405,404 385,434 L760,434 Z" fill="var(--purple-pale)"/>
      <path d="M760,88 C725,236 600,292 515,350 C470,380 442,410 428,434 L760,434 Z" fill="var(--paper)"/>
      <path d="M760,98 C728,246 606,300 524,356 C481,385 455,412 442,434 L760,434 Z" fill="var(--purple-deep)"/>
    </svg>

    <div class="brand">
      <span class="brand__initials">BVR</span>
      <span class="brand__name">MEDICAL, LLC</span>
    </div>

    <span class="divider" aria-hidden="true"></span>

    <div class="person">
      <p class="person__name">Dale Hopkins</p>
      <p class="person__role">Owner</p>
    </div>

    <ul class="contact">
      <li class="contact__item">
        <svg class="contact__icon" viewBox="0 0 16 16" aria-hidden="true"><rect x="4" y="1" width="8" height="14" rx="1.5" fill="none" stroke="var(--purple-deep)" stroke-width="1.6"/><circle cx="8" cy="12.3" r="0.9" fill="var(--purple-deep)"/></svg>
        901-555-0147
      </li>
      <li class="contact__item">
        <svg class="contact__icon" viewBox="0 0 16 16" aria-hidden="true"><rect x="1" y="3" width="14" height="10" rx="1" fill="var(--purple-deep)"/><path d="M1.5,3.5 L8,9 L14.5,3.5" fill="none" stroke="var(--paper)" stroke-width="1.3"/></svg>
        bvrmedllc@fernpostmail.com
      </li>
      <li class="contact__item">
        <svg class="contact__icon" viewBox="0 0 16 16" aria-hidden="true"><circle cx="8" cy="8" r="7" fill="var(--purple-deep)"/><path d="M1,8 H15 M8,1 C4,5 4,11 8,15 M8,1 C12,5 12,11 8,15" fill="none" stroke="var(--paper)" stroke-width="1"/></svg>
        www.bvrmedllc.net
      </li>
    </ul>
  </section>

  <section class="card card--back" aria-label="Card back">
    <svg class="card__wave" viewBox="0 0 760 434" aria-hidden="true">
      <g transform="translate(760 0) scale(-1 1)">
        <path d="M760,0 C730,150 600,230 500,300 C440,342 400,395 380,434 L760,434 Z" fill="var(--purple-pale)"/>
        <path d="M760,20 C735,180 610,255 520,318 C470,353 440,398 425,434 L760,434 Z" fill="var(--paper)"/>
        <path d="M760,32 C740,190 618,264 530,326 C482,360 454,402 440,434 L760,434 Z" fill="var(--purple-deep)"/>
      </g>
    </svg>
  </section>

</main>
</body>
</html>
```